New website: Veldrimoxtours.com

We need to build a website for our small travel agency.
We want to be able to upload our brochures and offer our tours on site. No online payments involved yet.

We want to create an exact copy of another website: www.trelqubanvoy.is, but with our own information and products. We like that design very much.

We are not going to do any sales via the website as the website above, but instead we want to show in the same style and everything the different tours that we offer.

We need to be able to modify tours: tour pictures, info, add videos, text, etc.

We need the website in English and Spanish. We can provide the Spanish translation.

We would advice you to create a copy of that website, with the text to be editable by us.
We own the website www.veldrimoxtours.com and need that the designer uploads it and makes it work as well.

We have uploaded some pictures that can be used as place markers.

I HAVE UPLOADED OUR BROCHURE DEMO SO YOU CAN GET MORE INFO IN ENGLISH ABOUT US AND MORE PICTURES.

PLEASE REMEMBER THAT THE WEBSITE ¨MOVES¨ when you resize it! Specially the pictures get ¨bigger¨ or smaller¨ when you resize. The same applies to the logos :-)

Once you have created the front page just as the original website I will select it and then we can put the real info and extra pages :-)

Target Market(s)

Tourists, international people traveling.

Industry/Entity Type

Tourism

Coding

Coded - Design and coding required

Number of Pages Required

5+ page

Font styles to use
Sans Serif

Colors
ffffff

Requirements
Must have
• Exactly the same layout of the website mentioned (www.trelqubanvoy.is)
• Everything the same, but with our own logo, texts and photos.
• HOME
• TOURS
• GROUPS
• OUR MOST POPULAR TOURS

```html
<!DOCTYPE html>
<html lang="en">
<head>
<meta charset="utf-8">
<title>Veldrimox Tours</title>
<link href="https://fonts.googleapis.com/css2?family=Alegreya:ital,wght@1,400&family=Alegreya+Sans:wght@400;500;700&family=Open+Sans:wght@400;600&display=swap" rel="stylesheet">
<style>
:root{
  --red:#e0262b;
  --green:#3a9d2f;
  --ink:#1f1f1f;
  --muted:#6a6a6a;
  --line:#d9d9d9;
  --white:#ffffff;
  --band-about:#f3f3f3;
  --band-mission:#e8e8e8;
  --band-vision:#f5f5f5;
  --footer:#231f20;
  --footer-text:#d8d8d8;
}
*{margin:0;padding:0;box-sizing:border-box}
html,body{width:1200px;height:3403px;overflow:hidden;background:var(--white)}
body{position:relative;font-family:"Open Sans",sans-serif;color:var(--ink)}
.abs{position:absolute}
a{color:inherit;text-decoration:none}

/* header */
.brand{left:131px;top:40px;font-family:"Alegreya Sans",sans-serif;font-weight:700;color:var(--ink);line-height:1}
.brand .b1{display:block;font-size:46px;letter-spacing:1px}
.brand .b2{display:block;font-size:30px;margin-left:72px;margin-top:2px}
.lang{left:987px;top:34px;width:79px;height:36px;border:1px solid var(--line);border-radius:3px;font-size:11px;display:flex;align-items:center;justify-content:center;gap:6px;color:var(--ink)}
.lang .dot{width:14px;height:14px;border-radius:50%;background:#3a4f9c}
.nav{top:98px;left:454px;display:flex;font-family:"Alegreya Sans",sans-serif;font-weight:500;font-size:15px;letter-spacing:.5px}
.nav a{position:absolute;white-space:nowrap}
.nav .active{color:var(--red)}

/* hero */
.photo{position:absolute}
.hero-title{font-family:"Alegreya",serif;font-style:italic;font-size:50px;color:var(--white);line-height:1}
.hero-sub{font-family:"Alegreya Sans",sans-serif;font-weight:500;font-size:23px;color:var(--white);margin-top:4px}

/* tours */
.section-title{font-family:"Alegreya Sans",sans-serif;font-weight:500;font-size:35px;color:var(--ink)}
.tabs{left:131px;top:733px;width:938px;height:38px;border-bottom:1px solid var(--line);font-family:"Alegreya Sans",sans-serif;font-size:14px}
.tabs span{position:absolute;top:0;white-space:nowrap;color:var(--ink)}
.tabs .active{color:var(--red)}
.tabs .active::after{content:"";position:absolute;left:0;right:0;top:35px;height:3px;background:var(--red)}
.card-frame{position:absolute;width:293px;height:254px;background:var(--white);padding:7px;box-shadow:0 1px 6px rgba(0,0,0,.25)}
.card-frame .photo{position:static;width:100%;height:100%}
.card-name{font-family:"Alegreya Sans",sans-serif;font-weight:500;font-size:24px;color:var(--ink)}
.card-len{font-family:"Alegreya Sans",sans-serif;font-size:19px;color:var(--muted)}
.card-price{font-family:"Alegreya Sans",sans-serif;font-weight:500;font-size:19px;color:var(--green)}
.btn{position:absolute;border:2px solid var(--red);background:var(--white);color:var(--red);font-family:"Alegreya Sans",sans-serif;font-weight:500;font-size:15px;display:flex;align-items:center;justify-content:center}

/* info bands */
.band{position:absolute;left:0;width:1200px}
.band-title{font-family:"Alegreya Sans",sans-serif;font-weight:500;font-size:40px;color:var(--ink)}
.band-text{font-size:13px;line-height:23px;color:#555;width:492px}
.band-text p+p{margin-top:16px}

/* partners */
.badge{position:absolute}

/* footer */
.footer{left:0;top:3123px;width:1200px;height:280px;background:var(--footer)}
.foot-logo{left:131px;top:3163px;width:232px;height:232px;border:4px solid var(--white);border-radius:50%;display:flex;flex-direction:column;align-items:center;justify-content:center;font-family:"Alegreya Sans",sans-serif;font-weight:700;color:var(--white);line-height:1}
.foot-logo .b1{font-size:34px}
.foot-logo .b2{font-size:24px;margin-top:4px}
.foot-col{font-family:"Alegreya Sans",sans-serif;font-size:12px;line-height:20px;color:var(--footer-text);text-transform:uppercase}
.copy{left:131px;top:3364px;font-size:11px;color:#8a8a8a;font-family:"Alegreya Sans",sans-serif}
</style>
</head>
<body>

<header>
  <div class="abs brand"><span class="b1">VELDRIMOX</span><span class="b2">TOURS</span></div>
  <div class="abs lang"><span class="dot"></span>ENG
    <svg width="8" height="6" viewBox="0 0 8 6"><path d="M1 1l3 3 3-3" fill="none" stroke="#333" stroke-width="1.2"/></svg>
  </div>
  <nav class="abs nav">
    <a class="active" style="left:0">HOME</a>
    <a style="left:86px">TOURS</a>
    <a style="left:179px">GROUPS</a>
    <a style="left:279px">RENT A CAR</a>
    <a style="left:408px">FLIGHT</a>
    <a style="left:505px">CONTACT</a>
    <svg style="position:absolute;left:603px;top:2px" width="14" height="14" viewBox="0 0 14 14"><circle cx="5.5" cy="5.5" r="4.3" fill="none" stroke="#1f1f1f" stroke-width="2"/><path d="M9 9l4 4" stroke="#1f1f1f" stroke-width="2.2"/></svg>
  </nav>
</header>

<section class="hero">
  <div class="photo" role="img" aria-label="Hikers looking at snowy granite peaks across a lake" style="left:0;top:166px;width:592px;height:449px;background:linear-gradient(180deg,#6f9bd0 0%,#b9cfe6 30%,#5e6670 55%,#7c8b93 70%,#3b3a33 100%)"></div>
  <div class="abs" style="left:131px;top:505px">
    <div class="hero-title">Specialized</div>
    <div class="hero-sub">Veldrimox Tours →</div>
  </div>
  <div class="photo" role="img" aria-label="Open road across the steppe towards distant mountains" style="left:601px;top:166px;width:599px;height:222px;background:linear-gradient(180deg,#7fa3cf 0%,#b5c9de 35%,#6e7a5c 60%,#565a46 100%)"></div>
  <div class="abs" style="left:624px;top:286px">
    <div class="hero-title">Independent</div>
    <div class="hero-sub">Veldrimox Tours →</div>
  </div>
  <div class="photo" role="img" aria-label="Mountain range above a dark valley" style="left:601px;top:397px;width:599px;height:218px;background:linear-gradient(180deg,#a7bfd9 0%,#d8e2ec 35%,#56606a 62%,#1f2124 100%)"></div>
  <div class="abs" style="left:624px;top:512px">
    <div class="hero-title">Receptive</div>
    <div class="hero-sub">Veldrimox Tours →</div>
  </div>
</section>

<section class="tours">
  <h2 class="abs section-title" style="left:0;width:1200px;text-align:center;top:650px">Our most popular tours</h2>
  <div class="abs tabs">
    <span class="active" style="left:0">Popular Tours</span>
    <span style="left:137px">Day Tours</span>
    <span style="left:255px">Travel by Air Tours</span>
    <span style="left:420px">Self Drive Tours</span>
    <span style="left:570px">Adventures Tours</span>
    <span style="left:731px">Customize Tours</span>
    <span style="left:885px">Transfer</span>
  </div>

  <div class="card-frame" style="left:131px;top:805px"><div class="photo" role="img" aria-label="Turquoise lake with snowy peaks" style="background:linear-gradient(180deg,#5f95cf 0%,#c4d6e8 40%,#6b7f86 58%,#1f7a8c 75%,#16566a 100%)"></div></div>
  <div class="card-frame" style="left:454px;top:805px"><div class="photo" role="img" aria-label="Hiker on a rocky trail facing granite spires" style="background:linear-gradient(180deg,#8fb0d4 0%,#dfe6ee 35%,#8f8573 60%,#6d7444 100%)"></div></div>
  <div class="card-frame" style="left:773px;top:805px"><div class="photo" role="img" aria-label="Trekker with a large backpack in a green valley" style="background:linear-gradient(180deg,#6fa0d6 0%,#a9c3df 35%,#7c9a52 65%,#4f6b30 100%)"></div></div>

  <div class="abs card-name" style="left:131px;top:1083px">Patagonia Chile</div>
  <div class="abs card-len" style="left:131px;top:1118px">length: 3 - 5 hours</div>
  <div class="abs card-price" style="left:131px;top:1147px">6.400 ISK</div>
  <div class="abs card-name" style="left:454px;top:1083px">Patagonia Chile</div>
  <div class="abs card-len" style="left:454px;top:1118px">length: 3 - 5 hours</div>
  <div class="abs card-price" style="left:454px;top:1147px">6.400 ISK</div>
  <div class="abs card-name" style="left:773px;top:1083px">Patagonia Chile</div>
  <div class="abs card-len" style="left:773px;top:1118px">length: 3 - 5 hours</div>
  <div class="abs card-price" style="left:773px;top:1147px">6.400 ISK</div>

  <div class="card-frame" style="left:131px;top:1222px"><div class="photo" role="img" aria-label="Hiker on a ridge above snowy mountains" style="background:linear-gradient(180deg,#3d74c2 0%,#8db1de 40%,#c9d2da 60%,#6f6a5e 100%)"></div></div>
  <div class="card-frame" style="left:454px;top:1222px"><div class="photo" role="img" aria-label="Hiker overlooking a glacial lake between peaks" style="background:linear-gradient(180deg,#7ea6d4 0%,#d6dee6 35%,#4e8a8c 65%,#3c5a3a 100%)"></div></div>
  <div class="card-frame" style="left:773px;top:1222px"><div class="photo" role="img" aria-label="Granite peaks above golden steppe" style="background:linear-gradient(180deg,#3f70b8 0%,#9ab8dc 40%,#8a8a86 60%,#a58a4e 100%)"></div></div>

  <div class="abs card-name" style="left:131px;top:1500px">Patagonia Chile</div>
  <div class="abs card-len" style="left:131px;top:1535px">length: 3 - 5 hours</div>
  <div class="abs card-price" style="left:131px;top:1564px">6.400 ISK</div>
  <div class="abs card-name" style="left:454px;top:1500px">Patagonia Chile</div>
  <div class="abs card-len" style="left:454px;top:1535px">length: 3 - 5 hours</div>
  <div class="abs card-price" style="left:454px;top:1564px">6.400 ISK</div>
  <div class="abs card-name" style="left:773px;top:1500px">Patagonia Chile</div>
  <div class="abs card-len" style="left:773px;top:1535px">length: 3 - 5 hours</div>
  <div class="abs card-price" style="left:773px;top:1564px">6.400 ISK</div>

  <a class="btn" style="left:483px;top:1633px;width:231px;height:57px">View All Our Popular Tours</a>
</section>

<section class="band" style="top:1735px;height:460px;background:var(--band-about)">
  <div class="photo" role="img" aria-label="Sunglasses, camera and backpack travel kit" style="left:0;top:40px;width:545px;height:380px;background:radial-gradient(ellipse at 55% 50%,#3a3a3a 0%,#8b8b8b 35%,rgba(243,243,243,0) 70%)"></div>
  <h2 class="abs band-title" style="left:576px;top:44px">About us</h2>
  <div class="abs band-text" style="left:576px;top:105px">
    <p>Veldrimox Tours is a new receptive tour operator specializing in the design and delivery of customized services incoming Pristine destinations in Sub-Antarctic ecoregion and Chilean Antarctica.</p>
    <p>We are a company formed by a qualified team that has high motivation, optimal training, high human capital and whose members have more than 10 years of experience working as Independent Tourism, National and International Regional Receptive. In all we empower and we meet the high demands for services Tourist required by our customers.</p>
  </div>
  <a class="btn" style="left:572px;top:363px;width:126px;height:57px">More About Us</a>
</section>

<section class="band" style="top:2195px;height:402px;background:var(--band-mission)">
  <h2 class="abs band-title" style="left:131px;top:62px">Our mission</h2>
  <div class="abs band-text" style="left:131px;top:117px">
    <p>Our mission is to offer Receptive Tourism for Region Magallanes and Chilean Antarctica that meet the quality requirements and human value that our customers request. To achieve this, we work together with selected tourism providers and focus towards excellent personalized service, serving with passion, experience and responsibility to each of our clients.</p>
  </div>
  <a class="btn" style="left:131px;top:268px;width:184px;height:57px">Contact us for More Info</a>
  <div class="photo" role="img" aria-label="Vintage suitcase with straw hat, camera and map" style="left:658px;top:20px;width:408px;height:340px;background:radial-gradient(ellipse at 50% 60%,#c76a1e 0%,#d9a36a 35%,rgba(232,232,232,0) 70%)"></div>
</section>

<section class="band" style="top:2597px;height:374px;background:var(--band-vision)">
  <div class="photo" role="img" aria-label="Old leather suitcase covered in travel stickers" style="left:131px;top:24px;width:368px;height:326px;background:radial-gradient(ellipse at 50% 55%,#6b3e22 0%,#8d5a35 45%,rgba(245,245,245,0) 72%)"></div>
  <h2 class="abs band-title" style="left:576px;top:60px">Our Vision</h2>
  <div class="abs band-text" style="left:576px;top:120px">
    <p>Our vision is to create a platform Logistics and Tourism Ecoregion Sub-Antarctic and Antarctic a whole tourist offer area through a local, national and global network of suppliers, with the aim improve, through careful selection of providers, accessibility by the customer, competitiveness in the market, facilitating the inclusion of small and medium businesses.</p>
  </div>
  <a class="btn" style="left:574px;top:268px;width:183px;height:57px">Contact us for More Info</a>
</section>

<section class="partners">
  <svg class="badge" style="left:150px;top:3008px" width="80" height="80" viewBox="0 0 80 80" aria-label="Partner badge"><circle cx="40" cy="40" r="38" fill="#e6e6e6" stroke="#9a9a9a" stroke-width="2"/></svg>
  <svg class="badge" style="left:578px;top:3005px" width="50" height="86" viewBox="0 0 50 86" aria-label="Partner badge"><rect x="1" y="1" width="48" height="84" fill="#555"/></svg>
  <svg class="badge" style="left:966px;top:3014px" width="88" height="64" viewBox="0 0 88 64" aria-label="Partner badge"><rect x="1" y="1" width="86" height="62" fill="#e6e6e6" stroke="#9a9a9a" stroke-width="2"/></svg>
</section>

<footer>
  <div class="abs footer"></div>
  <div class="abs foot-logo"><span class="b1">VELDRIMOX</span><span class="b2">TOURS</span></div>
  <div class="abs foot-col" style="left:447px;top:3170px">Home<br>Tours<br>Groups<br>Rent a car<br>Flight<br>Contact</div>
  <div class="abs foot-col" style="left:615px;top:3170px">How to book<br>Booking terms<br>Privacy policy</div>
  <div class="abs foot-col" style="left:862px;top:3170px">Veldrimoxtours<br>a1868 nemo enim ipsam voluptatem<br>quia<br>voluptas sit aspernatur<br><br>+354 555 0142<br>info@veldrimoxtours.com</div>
  <div class="abs copy">© 2016, VELDRIMOXTOURS.COM</div>
</footer>

</body>
</html>
```